Master slides for standard ppt presentation

I just my company, went through GlyphMeadow for the log design and already have an identity that I like.
I need to transpose this identity into some nice Master slides for Powerpoint presentation. I want it clean, with fresh color connection to my logo, not over crowded and obviously different vs what powerpoint proposes as standard design ideas. I will attach a few materials that I already use, branded with the company logo so that you can take inspiration.

```html
<!DOCTYPE html>
<html lang="en">
<head>
<meta charset="utf-8">
<title>Verdanor – Master Slides</title>
<link href="https://fonts.googleapis.com/css2?family=Poppins:ital,wght@0,500;0,700;0,800;1,600;1,700;1,800&family=Roboto:wght@400;500;700&display=swap" rel="stylesheet">
<style>
:root{
  --bg:#d5d6d8;
  --ink:#134845;
  --ink-deep:#0f3d3a;
  --green:#3fae8a;
  --green-light:#5ec49a;
  --grey:#a9acae;
  --text:#4b5552;
  --white:#ffffff;
}
*{margin:0;padding:0;box-sizing:border-box}
html,body{width:906px;height:1200px;overflow:hidden;background:var(--bg)}
.sheet{position:absolute;left:0;top:0;width:1669px;height:2212px;transform:scale(.5428);transform-origin:0 0;font-family:"Roboto",sans-serif}
.slide{position:absolute;width:510px;height:287px;background:var(--white);overflow:hidden;box-shadow:0 10px 18px rgba(0,0,0,.16)}
.slide--dark{background:var(--ink)}
.abs{position:absolute}
.footer{position:absolute;left:0;right:0;bottom:0;height:15px;background:var(--ink);color:var(--white);font-size:6px;text-align:center;line-height:15px}
.brand{position:absolute;font-family:"Poppins",sans-serif;font-weight:800;color:var(--ink);letter-spacing:.02em;line-height:1}
.photo{position:absolute}
.heading{font-family:"Roboto",sans-serif;font-weight:700;color:var(--ink);line-height:1}
.sub{font-weight:400;color:var(--text);line-height:1.1}
.body-copy{font-size:7px;line-height:12.6px;color:var(--text);text-align:justify}
.rule{width:32px;height:3px;background:var(--green)}
.about{font-family:"Poppins",sans-serif;font-style:italic;font-weight:800;font-size:36px;line-height:1}
.about-title{font-family:"Poppins",sans-serif;font-style:italic;font-weight:700;font-size:21px;line-height:1.2}
.about-sub{font-family:"Poppins",sans-serif;font-style:italic;font-weight:600;font-size:12.5px}
.toc-num{position:absolute;width:34px;height:34px;border-radius:50%;background:var(--ink);color:var(--white);font:700 12px/34px "Roboto",sans-serif;text-align:center;box-shadow:0 0 0 4px #e6ebea}
.toc-item{position:absolute;left:272px;width:210px}
.toc-item h4{font-size:8px;font-weight:700;color:var(--ink)}
.toc-item p{font-size:4.8px;line-height:6px;color:var(--text);margin-top:2px}
.contact-line{display:flex;align-items:center;gap:6px;font-size:16px;color:var(--white);line-height:21px}
.dot-icon{width:13px;height:13px;border-radius:50%;background:var(--white)}
</style>
</head>
<body>
<div class="sheet">

  <!-- Cover, photo style -->
  <section class="slide" style="left:289px;top:141px">
    <div class="photo" role="img" aria-label="City skyline at the waterfront under a teal tint" style="inset:0;background:linear-gradient(180deg,#63c79c 0%,#3a9a86 55%,#2b8f85 100%)"></div>
    <div class="brand" style="left:44px;top:88px;font-size:16px;color:var(--white)">VERDANOR</div>
    <div class="abs about" style="left:44px;top:155px;color:var(--white)">About</div>
    <div class="abs about-title" style="left:44px;top:190px;color:var(--white)">Title Presentation</div>
    <div class="abs rule" style="left:44px;top:222px;background:var(--white);height:2px"></div>
    <div class="abs about-sub" style="left:44px;top:229px;color:var(--white)">Sub Title Presentation Goes Here</div>
  </section>

  <!-- Cover, light -->
  <section class="slide" style="left:869px;top:141px">
    <div class="brand" style="left:31px;top:95px;font-size:16px">VERDANOR</div>
    <div class="abs about" style="left:32px;top:160px;color:var(--ink)">About</div>
    <div class="abs about-title" style="left:33px;top:194px;color:var(--ink)">Title Presentation</div>
    <div class="abs rule" style="left:33px;top:226px;height:2px"></div>
    <div class="abs about-sub" style="left:31px;top:234px;color:#7c8683">Sub Title Presentation Goes Here</div>
    <div class="footer">Copyright © 2023 verdanor</div>
  </section>

  <!-- Brand intro with curved panel -->
  <section class="slide" style="left:289px;top:469px;height:290px">
    <svg class="abs" width="510" height="290" style="left:0;top:0"><path d="M212,0 Q290,145 212,290 L510,290 L510,0 Z" fill="var(--ink)"/></svg>
    <div class="brand" style="left:33px;top:196px;font-size:33px">VERDANOR</div>
    <div class="abs" style="left:40px;top:253px;display:flex;gap:6px">
      <span style="width:15px;height:15px;border-radius:50%;background:var(--ink)"></span>
      <span style="width:15px;height:15px;border-radius:50%;background:var(--ink)"></span>
      <span style="width:15px;height:15px;border-radius:50%;background:var(--ink)"></span>
    </div>
    <div class="abs" style="left:284px;top:30px;width:196px">
      <div class="heading" style="font-size:20px;color:var(--white);font-weight:500">Heading Here</div>
      <div class="sub" style="font-size:11px;color:#dfe8e6">Sub Heading</div>
      <p class="body-copy" style="color:#e3ecea;margin-top:16px;font-size:6.6px;line-height:10.5px">Our team builds clear growth plans for every client, pairing careful research with steady delivery so each project moves forward with purpose and measurable results across every quarter.</p>
      <p class="body-copy" style="color:#e3ecea;margin-top:46px;font-size:6.6px;line-height:10.5px">We listen first, then shape simple strategies that turn ideas into lasting value for partners.</p>
    </div>
  </section>

  <!-- Dark text slide -->
  <section class="slide slide--dark" style="left:869px;top:469px;height:290px">
    <div class="brand" style="left:408px;top:28px;font-size:12px;color:var(--green-light)">VERDANOR</div>
    <div class="abs" style="left:46px;top:46px;width:168px">
      <div class="heading" style="font-size:16px;color:var(--white);font-weight:500">Heading Here</div>
      <div class="sub" style="font-size:9px;color:#dfe8e6">Sub Heading</div>
      <p class="body-copy" style="color:#d9e4e1;margin-top:14px;font-size:5.8px;line-height:9px">Our team builds clear growth plans for every client, pairing careful research with steady delivery so each project moves forward with purpose and measurable results across every quarter.</p>
      <p class="body-copy" style="color:#d9e4e1;margin-top:40px;font-size:5.8px;line-height:9px">We listen first, then shape simple strategies that turn ideas into lasting value for partners.</p>
    </div>
  </section>

  <!-- Chart slide -->
  <section class="slide" style="left:289px;top:800px">
    <div class="abs" style="left:31px;top:25px">
      <div class="heading" style="font-size:21px;font-weight:500">Heading Here</div>
      <div class="sub" style="font-size:11px">Sub Heading</div>
    </div>
    <div class="brand" style="left:420px;top:48px;font-size:11px">VERDANOR</div>
    <svg class="abs" width="510" height="287" style="left:0;top:0" font-family="Roboto, sans-serif">
      <defs><linearGradient id="barGreen" x1="0" y1="0" x2="0" y2="1"><stop offset="0" stop-color="#5ec49a"/><stop offset="1" stop-color="#2f9a80"/></linearGradient></defs>
      <g stroke="#e3e5e5" stroke-width="1">
        <line x1="63" y1="82" x2="462" y2="82"/><line x1="63" y1="108" x2="462" y2="108"/>
        <line x1="63" y1="135" x2="462" y2="135"/><line x1="63" y1="161" x2="462" y2="161"/>
        <line x1="63" y1="187" x2="462" y2="187"/><line x1="63" y1="214" x2="462" y2="214" stroke="#bfc3c2"/>
      </g>
      <g font-size="6" fill="#8a9290" text-anchor="end">
        <text x="60" y="84">125</text><text x="60" y="110">100</text><text x="60" y="137">75</text>
        <text x="60" y="163">50</text><text x="60" y="189">25</text><text x="60" y="216">0</text>
      </g>
      <rect x="81" y="196" width="18" height="18" fill="var(--grey)"/>
      <rect x="104" y="157" width="19" height="57" fill="var(--ink)"/>
      <rect x="128" y="177" width="20" height="37" fill="url(#barGreen)"/>
      <rect x="179" y="187" width="20" height="27" fill="var(--grey)"/>
      <rect x="203" y="169" width="20" height="45" fill="url(#barGreen)"/>
      <rect x="227" y="132" width="20" height="82" fill="var(--ink)"/>
      <rect x="277" y="158" width="20" height="56" fill="url(#barGreen)"/>
      <rect x="301" y="141" width="20" height="73" fill="var(--ink)"/>
      <rect x="326" y="183" width="20" height="31" fill="var(--grey)"/>
      <rect x="376" y="114" width="20" height="100" fill="var(--ink)"/>
      <rect x="401" y="153" width="20" height="61" fill="url(#barGreen)"/>
      <rect x="425" y="186" width="20" height="28" fill="var(--grey)"/>
      <g font-size="6" fill="#8a9290" text-anchor="middle"><text x="117" y="227">April</text><text x="199" y="227">May</text></g>
      <g font-size="5" fill="#8a9290">
        <rect x="78" y="257" width="6" height="6" fill="var(--ink)"/><text x="91" y="262">Unique Infographic</text>
        <rect x="174" y="257" width="6" height="6" fill="var(--ink)"/><text x="187" y="262">Unique Infographic</text>
        <rect x="270" y="257" width="6" height="6" fill="var(--ink)"/><text x="283" y="262">Unique Infographic</text>
        <rect x="366" y="257" width="6" height="6" fill="#c9cccb"/><text x="379" y="262">Unique Infographic</text>
      </g>
    </svg>
  </section>

  <!-- Table of content -->
  <section class="slide" style="left:869px;top:800px;width:511px">
    <div class="photo" role="img" aria-label="Photo of young colleagues gathered around a laptop" style="left:0;top:0;width:243px;height:272px;background:linear-gradient(135deg,#cfcac4,#8d8a86 55%,#3f4a55)"></div>
    <div class="abs heading" style="left:272px;top:22px;font-size:14px">TABLE OF CONTENT</div>
    <div class="abs rule" style="left:272px;top:44px;height:2px"></div>
    <div class="brand" style="left:446px;top:44px;font-size:9px">VERDANOR</div>
    <div class="toc-num" style="left:225px;top:64px">01</div>
    <div class="toc-num" style="left:225px;top:112px">02</div>
    <div class="toc-num" style="left:225px;top:161px">03</div>
    <div class="toc-num" style="left:225px;top:209px">04</div>
    <div class="toc-item" style="top:66px"><h4>LOREM IPSUM</h4><p>Short note describing this section of the presentation.</p></div>
    <div class="toc-item" style="top:114px"><h4>LOREM IPSUM</h4><p>Short note describing this section of the presentation.</p></div>
    <div class="toc-item" style="top:163px"><h4>LOREM IPSUM</h4><p>Short note describing this section of the presentation.</p></div>
    <div class="toc-item" style="top:211px"><h4>LOREM IPSUM</h4><p>Short note describing this section of the presentation.</p></div>
    <div class="footer">Copyright © 2023 verdanor</div>
  </section>

  <!-- Section text slide -->
  <section class="slide" style="left:289px;top:1128px;height:286px">
    <div class="brand" style="left:24px;top:50px;font-size:10px">VERDANOR</div>
    <div class="abs" style="left:44px;top:130px">
      <div class="heading" style="font-size:27px;font-weight:500">Heading Here</div>
      <div class="sub" style="font-size:15px">Sub Heading</div>
    </div>
    <div class="abs" style="left:253px;top:68px;width:214px">
      <p class="body-copy">Our team builds clear growth plans for every client, pairing careful research with steady delivery so each project moves forward with purpose and measurable results across every quarter.</p>
      <p class="body-copy" style="margin-top:36px">We listen first, then shape simple strategies that turn ideas into lasting value for partners.</p>
    </div>
    <div class="footer">Copyright © 2023 verdanor</div>
  </section>

  <!-- Text with photo right -->
  <section class="slide" style="left:869px;top:1128px;height:286px">
    <div class="abs" style="left:32px;top:42px">
      <div class="heading" style="font-size:21px;font-weight:500">Heading Here</div>
      <div class="sub" style="font-size:11px">Sub Heading</div>
    </div>
    <div class="abs rule" style="left:32px;top:82px;height:2px"></div>
    <p class="abs body-copy" style="left:32px;top:110px;width:198px">Our team builds clear growth plans for every client, pairing careful research with steady delivery so each project moves forward with purpose and measurable results across every quarter.</p>
    <div class="photo" role="img" aria-label="Photo of a group of smiling coworkers around a laptop" style="left:268px;top:0;width:242px;height:271px;background:linear-gradient(160deg,#e9e4de,#a89384 45%,#3b3533)"></div>
    <div class="footer">Copyright © 2023 verdanor</div>
  </section>

  <!-- Thanks -->
  <section class="slide slide--dark" style="left:289px;top:1456px;height:290px;color:var(--white);text-align:center">
    <div class="abs" style="left:0;right:0;top:50px;font-size:47px;line-height:57px;font-weight:500">Thanks<br>For Wathing</div>
    <div class="abs" style="left:0;right:0;top:180px;font-size:14.5px;line-height:18.5px">Alder Bay, Western Australia<br><b style="font-weight:500">P :</b> 0040 700 000 123&nbsp;&nbsp; <b style="font-weight:500">E :</b> lucien.marchal@verdanor.ro<br>www.verdanor.ro</div>
  </section>

  <!-- Text with photo left -->
  <section class="slide" style="left:869px;top:1454px;height:286px">
    <div class="photo" role="img" aria-label="Photo of two colleagues working together at a laptop" style="left:0;top:0;width:242px;height:271px;background:linear-gradient(135deg,#d9dcd6,#a2a49b 50%,#55534e)"></div>
    <div class="abs" style="left:272px;top:20px">
      <div class="heading" style="font-size:20px;font-weight:500">Heading Here</div>
      <div class="sub" style="font-size:11px">Sub Heading</div>
    </div>
    <div class="brand" style="left:445px;top:48px;font-size:9px">VERDANOR</div>
    <div class="abs" style="left:272px;top:75px;width:214px">
      <p class="body-copy">Our team builds clear growth plans for every client, pairing careful research with steady delivery so each project moves forward with purpose and measurable results across every quarter.</p>
      <p class="body-copy" style="margin-top:36px">We listen first, then shape simple strategies that turn ideas into lasting value for partners.</p>
    </div>
    <div class="footer">Copyright © 2023 verdanor</div>
  </section>

  <!-- Icon set -->
  <section class="slide" style="left:289px;top:1788px;width:505px;height:283px">
    <div role="img" aria-label="Grid of small black pictogram icons for use in slides" class="abs" style="left:44px;top:28px;width:418px;height:232px;background:linear-gradient(180deg,#e4e6e6,#d9dcdc)"></div>
  </section>

  <!-- Contact slide -->
  <section class="slide" style="left:869px;top:1782px;height:289px">
    <svg class="abs" width="510" height="289" style="left:0;top:0"><path d="M214,0 Q290,145 214,289 L510,289 L510,0 Z" fill="var(--ink)"/></svg>
    <div class="brand" style="left:33px;top:196px;font-size:33px">VERDANOR</div>
    <div class="abs" style="left:275px;top:32px;color:var(--white)">
      <div style="font-family:'Poppins',sans-serif;font-weight:800;font-size:30px;line-height:1">Lucien Marchal</div>
      <div style="font-family:'Poppins',sans-serif;font-weight:500;font-size:19px;margin-top:4px">Managing Patner</div>
      <div style="font-size:16px;line-height:18px;margin-top:55px">48 Harbour Crest Road,<br>Maplewood, ON L5T 3K8</div>
      <div style="margin-top:14px">
        <div class="contact-line"><span class="dot-icon"></span>0040 700 000 123</div>
        <div class="contact-line"><span class="dot-icon"></span>lucien.marchal@verdanor.ro</div>
        <div class="contact-line"><span class="dot-icon"></span>www.verdanor.ro</div>
      </div>
    </div>
  </section>

</div>
</body>
</html>
```